Business Card design for construction company

I would like a business card design for a construction company - Harlow Constructions. I have attached the ai logo file for use. I would like the card to be very smart and clean and incorporate only white and the two colours in the logo. I would like the card to have two sides. One side can just have the logo, the other with the relevant information.

Target Market(s)

Building and Construction Clients

Industry/Entity Type

Business

Contact Information for Business Card

Name: Tom Pardoe
Company: Harlow Constructions Pty Limited
Address: 14 Mallee Crescent Carrow Vale 2093
Phone: 0427 531 068
Email: tomp@harlowbuild-example.com.au

Font styles to use
Serif
Sans Serif

Requirements
Must have
• Details noted above
• Logo as provided
• Colours as in logo
• Square edges
• A font that compliments the logo
Should not have
• Any colour other than white and those in logo
• Rounded edges

```html
<!DOCTYPE html>
<html lang="en">
<head>
<meta charset="utf-8">
<title>Harlow Constructions – Business Card</title>
<link rel="stylesheet" href="https://fonts.googleapis.com/css2?family=Oswald:wght@600&family=Roboto+Condensed:wght@300;400;700&display=swap">
<style>
  :root {
    --brand-blue: #00aeef;
    --ink: #111111;
    --logo-grey: #4a4a4a;
    --paper: #f3f3f3;
    --paper-shade: #e4e4e4;
    --white: #ffffff;
    --backdrop: #1e1e1e;
  }
  * { box-sizing: border-box; margin: 0; padding: 0; }
  html, body {
    width: 1200px; height: 1000px; overflow: hidden;
    background: var(--backdrop);
  }
  .canvas {
    width: 1200px; height: 1000px;
    display: flex; flex-direction: column; align-items: center; justify-content: center;
    gap: 40px;
  }
  .card {
    position: relative;
    width: 760px; height: 434px;
    overflow: hidden;
  }
  .wordmark {
    font-family: "Roboto Condensed", sans-serif;
    font-weight: 300;
    font-size: 40px;
    letter-spacing: 6px;
    text-transform: uppercase;
    white-space: nowrap;
  }

  /* Front */
  .card--front {
    background: var(--brand-blue);
    display: flex; align-items: center; justify-content: center;
  }
  .card--front .wordmark { color: var(--white); }

  /* Back */
  .card--back {
    background: linear-gradient(135deg, var(--paper) 0%, var(--white) 45%, var(--paper-shade) 100%);
  }
  .card--back .wordmark {
    position: absolute; left: 0; right: 0; top: 80px;
    text-align: center;
    color: var(--logo-grey);
  }
  .info-band {
    position: absolute; left: 0; right: 0; top: 196px; height: 172px;
    background: var(--brand-blue);
    display: flex; align-items: center;
  }
  .holder-name {
    width: 330px;
    text-align: center;
    font-family: "Oswald", sans-serif;
    font-weight: 600;
    font-size: 30px;
    text-transform: uppercase;
    color: var(--ink);
    letter-spacing: 0.5px;
  }
  .band-divider {
    width: 1px; height: 118px;
    background: var(--white);
    margin-right: 24px;
  }
  .contact {
    font-family: "Roboto Condensed", sans-serif;
    color: var(--ink);
    font-size: 17px;
    line-height: 1.25;
  }
  .contact__company {
    font-weight: 700;
    font-size: 18px;
    margin-bottom: 4px;
  }
  .contact__row {
    display: flex; align-items: flex-start; gap: 8px;
  }
  .contact__row svg {
    flex: none; width: 14px; height: 14px; margin-top: 3px;
    fill: var(--white);
  }
</style>
</head>
<body>
<main class="canvas">
  <section class="card card--front" aria-label="Card front">
    <span class="wordmark">Harlow Constructions</span>
  </section>

  <section class="card card--back" aria-label="Card back">
    <span class="wordmark">Harlow Constructions</span>
    <div class="info-band">
      <p class="holder-name">Tom Pardoe</p>
      <span class="band-divider"></span>
      <div class="contact">
        <p class="contact__company">Harlow Constructions Pty Limited</p>
        <div class="contact__row">
          <svg viewBox="0 0 24 24" aria-hidden="true"><path d="M12 2a7 7 0 0 0-7 7c0 5.2 7 13 7 13s7-7.8 7-13a7 7 0 0 0-7-7zm0 9.5A2.5 2.5 0 1 1 12 6.5a2.5 2.5 0 0 1 0 5z"/></svg>
          <p>14 Mallee Crescent<br>Carrow Vale 2093</p>
        </div>
        <div class="contact__row">
          <svg viewBox="0 0 24 24" aria-hidden="true"><path d="M6.6 10.8a15.1 15.1 0 0 0 6.6 6.6l2.2-2.2a1 1 0 0 1 1-.25 11.4 11.4 0 0 0 3.6.57 1 1 0 0 1 1 1V20a1 1 0 0 1-1 1A17 17 0 0 1 3 4a1 1 0 0 1 1-1h3.5a1 1 0 0 1 1 1c0 1.25.2 2.45.57 3.6a1 1 0 0 1-.25 1z"/></svg>
          <p>0427 531 068</p>
        </div>
        <div class="contact__row">
          <svg viewBox="0 0 24 24" aria-hidden="true"><path d="M3 5h18v14H3zm2 2v.5l7 4.5 7-4.5V7zm0 2.9V17h14V9.9l-7 4.5z"/></svg>
          <p>tomp@harlowbuild-example.com.au</p>
        </div>
      </div>
    </div>
  </section>
</main>
</body>
</html>
```